Korbel Medical Business Card Design

This is a private medical device company. We recently launched the new website and would like to redesign the business cards. Please see the website: www.korbelmedical-demo.com. We'd like to keep the cards simple and professional but modern to match the website and collateral branding. Our customers are physicians and investors. I have attached the old design for comparison. I have also attached the updated logo. Please note the business card information will change, based on all employees who need to order them. So I will need to be able easily edit the copy.
Updates

Hi designers-thank you very much for submitting designs. I look forward to the results!! Jodi

Target Market(s)

Our target audience are physicians

Industry/Entity Type

Medical

Contact Information for Business Card

Denise Halvorsen
Director of Marketing and Reimbursement
dhalvorsen@korbelmedical-demo.com
M: xxx-xxx-xxxx
O: xxx-xxx-xxxx
4120 Lark Mill Rd.
Suite 380
Austin, TX 78759

Font styles to use
Sans Serif

Requirements
Must have
• Must include the logo and a color or color from the logo and branding
Nice to have
• Maybe include the logo icon on the back.

```html
<!DOCTYPE html>
<html lang="en">
<head>
<meta charset="utf-8">
<title>Korbel Medical Business Cards</title>
<link rel="stylesheet" href="https://fonts.googleapis.com/css2?family=Exo+2:wght@400;500;600&display=swap">
<style>
  :root {
    --page-bg: #e9e7e4;
    --card-white: #f5f5f5;
    --card-dark: #4a4546;
    --accent-red: #e8294a;
    --accent-teal: #6fb3c4;
    --text-dark: #3d393a;
    --text-light: #ffffff;
  }
  * { margin: 0; padding: 0; box-sizing: border-box; }
  html, body {
    width: 1200px; height: 828px; overflow: hidden;
    background: var(--page-bg);
    font-family: "Exo 2", sans-serif;
  }
  .stage {
    position: relative; width: 1200px; height: 828px;
  }
  .card {
    position: absolute; top: 260px;
    width: 540px; height: 309px;
    overflow: hidden;
    border-radius: 3px;
    box-shadow: 0 10px 28px rgba(0,0,0,.18), 0 2px 4px rgba(0,0,0,.12);
  }
  .card-back { left: 40px; }
  .card-front { left: 620px; }
  .card-art { position: absolute; inset: 0; }

  .brand {
    position: absolute;
    display: flex; align-items: center; gap: 12px;
    color: var(--text-dark);
    font-weight: 500;
    letter-spacing: .5px;
  }
  .brand-dot {
    border-radius: 50%;
    background: var(--accent-teal);
  }
  .card-back .brand { left: 0; right: 0; top: 62px; justify-content: center; font-size: 26px; }
  .card-back .brand-dot { width: 24px; height: 24px; }
  .card-front .brand { left: 34px; top: 226px; font-size: 30px; }
  .card-front .brand-dot { width: 26px; height: 26px; }

  .website-band {
    position: absolute; left: 170px; top: 246px;
    color: var(--text-light);
    font-size: 15px; letter-spacing: 4.5px;
  }

  .contact-block {
    position: absolute; right: 24px; top: 26px;
    text-align: right; color: var(--text-light);
  }
  .person-name { font-size: 17px; font-weight: 600; letter-spacing: 1px; }
  .person-title { font-size: 11px; margin-top: 2px; }
  .address { font-size: 11px; line-height: 15px; margin-top: 22px; }
  .contact-list { list-style: none; margin-top: 14px; font-size: 9.5px; }
  .contact-list li {
    display: flex; justify-content: flex-end; align-items: center;
    gap: 7px; height: 17px;
  }
  .contact-icon { width: 10px; height: 10px; flex: none; }
</style>
</head>
<body>
<main class="stage">

  <section class="card card-back" aria-label="Card back">
    <svg class="card-art" viewBox="0 0 540 309" aria-hidden="true">
      <rect width="540" height="309" fill="var(--card-white)"/>
      <path d="M0,192 Q300,142 540,30 L540,309 L0,309 Z" fill="var(--accent-red)"/>
      <path d="M0,200 Q300,151 540,40 L540,309 L0,309 Z" fill="var(--card-dark)"/>
    </svg>
    <div class="brand"><span class="brand-dot"></span>Korbel Medical</div>
    <p class="website-band">www.korbelmedical-demo.com</p>
  </section>

  <section class="card card-front" aria-label="Card front">
    <svg class="card-art" viewBox="0 0 540 309" aria-hidden="true">
      <rect width="540" height="309" fill="var(--card-dark)"/>
      <path d="M0,87 Q350,110 442,309 L0,309 Z" fill="var(--accent-red)"/>
      <path d="M0,95 Q338,120 430,309 L0,309 Z" fill="var(--card-white)"/>
    </svg>

    <div class="contact-block">
      <p class="person-name">MARCUS ELLERY</p>
      <p class="person-title">Managing Director</p>
      <p class="address">4120 Lark Mill Rd.<br>Suite 380</p>
      <ul class="contact-list">
        <li>512 555 0148
          <svg class="contact-icon" viewBox="0 0 10 10" aria-hidden="true"><path d="M2,1 L4,1 L4.6,3 L3.4,3.8 Q4.4,5.8 6.2,6.6 L7,5.4 L9,6 L9,8 Q9,9 8,9 Q1,8.4 1,2 Q1,1 2,1 Z" fill="#fff"/></svg></li>
        <li>512 555 0193
          <svg class="contact-icon" viewBox="0 0 10 10" aria-hidden="true"><rect x="2.5" y=".5" width="5" height="9" rx="1" fill="none" stroke="#fff"/><circle cx="5" cy="8" r=".6" fill="#fff"/></svg></li>
        <li>512 555 0176
          <svg class="contact-icon" viewBox="0 0 10 10" aria-hidden="true"><rect x="1" y="4" width="8" height="5" fill="#fff"/><rect x="2.5" y="1" width="5" height="3" fill="none" stroke="#fff"/></svg></li>
        <li>mellery@korbelmedical-demo.com
          <svg class="contact-icon" viewBox="0 0 10 10" aria-hidden="true"><rect x=".5" y="2" width="9" height="6" fill="#fff"/><path d="M.5,2 L5,5.5 L9.5,2" fill="none" stroke="var(--card-dark)" stroke-width=".8"/></svg></li>
        <li>www.korbelmedical-demo.com
          <svg class="contact-icon" viewBox="0 0 10 10" aria-hidden="true"><g fill="none" stroke="#fff" stroke-width=".8"><circle cx="5" cy="5" r="4.2"/><ellipse cx="5" cy="5" rx="1.8" ry="4.2"/><path d="M.8,5 H9.2"/></g></svg></li>
      </ul>
    </div>

    <div class="brand"><span class="brand-dot"></span>Korbel Medical</div>
  </section>

</main>
</body>
</html>
```